Education Certificate

We need a modern yet professional Certificate for those who successfully pass / complete our online Training course.

There are various courses but ONE certificate design required.

the certificate needs to look extremely professional and of value.

```html
<!DOCTYPE html>
<html lang="en">
<head>
<meta charset="utf-8">
<title>Training Programme Certificate</title>
<link rel="stylesheet" href="https://fonts.googleapis.com/css2?family=UnifrakturMaguntia&family=VT323&display=swap">
<style>
  :root {
    --page: #ffffff;
    --gold-pale: #ffe27a;
    --gold: #ffc300;
    --gold-deep: #8a6d00;
    --ink: #000000;
    --paper-line: #ffffff;
    --text-light: #ffffff;
  }
  html, body {
    margin: 0;
    padding: 0;
    width: 1169px;
    height: 1200px;
    overflow: hidden;
    background: var(--page);
  }
  .certificate {
    display: block;
    width: 1169px;
    height: 1200px;
  }
  .frame-outer { fill: var(--gold-pale); }
  .frame-gold { fill: var(--gold); }
  .frame-line { fill: var(--paper-line); }
  .frame-inner { fill: var(--ink); }
  .title,
  .seal-word {
    font-family: "UnifrakturMaguntia", serif;
    fill: var(--text-light);
    stroke: var(--ink);
    stroke-width: 2;
    paint-order: stroke;
  }
  .title { font-size: 132px; letter-spacing: 2px; }
  .seal-word { font-size: 84px; }
  .detail {
    font-family: "VT323", monospace;
    fill: var(--text-light);
    font-size: 38px;
  }
</style>
</head>
<body>
<svg class="certificate" viewBox="0 0 1300 1334" preserveAspectRatio="none" xmlns="http://www.w3.org/2000/svg">
  <defs>
    <radialGradient id="emblem-tone" cx="50%" cy="50%" r="50%">
      <stop offset="0%" stop-color="#000000"/>
      <stop offset="30%" stop-color="#ffc300" stop-opacity="0.9"/>
      <stop offset="55%" stop-color="#000000"/>
      <stop offset="80%" stop-color="#e0ac00" stop-opacity="0.85"/>
      <stop offset="100%" stop-color="#8a6d00" stop-opacity="0.9"/>
    </radialGradient>
  </defs>

  <g class="frame">
    <polygon class="frame-outer" points="68,520 180,422 1160,422 1262,530 1262,912 1140,1022 175,1022 68,920"/>
    <polygon class="frame-gold" points="76,522 183,430 1156,430 1254,533 1254,908 1137,1014 178,1014 76,916"/>
    <polygon class="frame-line" points="86,524 186,440 1152,440 1244,535 1244,906 1133,1004 182,1004 86,912"/>
    <polygon class="frame-gold" points="92,525 188,446 1150,446 1238,533 1238,906 1134,999 185,999 92,910"/>
    <polygon class="frame-inner" points="98,525 190,451 1147,451 1232,532 1232,905 1133,994 188,994 98,905"/>
  </g>

  <g class="emblem" role="img" aria-label="Gold star-burst emblem of overlapping rotated squares">
    <circle cx="647" cy="718" r="292" fill="url(#emblem-tone)"/>
  </g>

  <text class="title" x="685" y="560" text-anchor="middle">Certificate</text>
  <text class="seal-word" x="643" y="752" text-anchor="middle">pass</text>

  <text class="detail" x="98" y="762">training program</text>
  <text class="detail" x="970" y="740">from 22-03-2024</text>
  <text class="detail" x="970" y="772">to 22-06-2024</text>

  <text class="detail" x="668" y="970" text-anchor="middle">It  is certified the Mr. Tomas Successfully completed</text>
</svg>
</body>
</html>
```